Flyer for my cleaning business

Business name: Velmond Cleaning Services
Contact: 318.492.5063
Email: [login to view URL]

I would like the flyer to say this information!!!! PREFERRED COLORS GREEN, BLUE AND YELLOW.

LET US DO THE DIRTY WORK FOR YOU!
You have better things to do than clean.
Satisfaction guaranteed
Flexible scheduling
Affordable pricing
Hight quality service

Full house cleaning, Professional organizing, Window Cleaning, Blind cleaning, Event cleaning.

We bring the supplies!

COUPONS:

HOMECLEANING
$25.00 OFF
First home cleaning service code 7777
exp 11/17/19

PROFESSIONAL ORGANIZING
$20.00 OFF
CODE 7778
EXP 11/17/19

WINDOW CLEANING
$30.00 OFF
CODE 7779
EXP 11/17/19

VELMOND CLEANING SERVICES. 318.492.5063

```html
<!DOCTYPE html>
<html lang="en">
<head>
<meta charset="utf-8">
<title>Velmond Cleaning Services – Flyer</title>
<link href="https://fonts.googleapis.com/css2?family=Roboto+Condensed:wght@400;700&family=Lato:wght@400;700;900&display=swap" rel="stylesheet">
<style>
  :root {
    --page-bg: #eef2ea;
    --paper: #ffffff;
    --green: #8cc63f;
    --green-dark: #6a9a2c;
    --teal: #1f7f93;
    --cyan: #2bb8e0;
    --ink: #222222;
    --muted: #555555;
    --photo-light: #e9ece6;
    --photo-mid: #b9c98a;
  }
  * { box-sizing: border-box; margin: 0; padding: 0; }
  html, body { width: 932px; height: 1200px; overflow: hidden; background: var(--page-bg); }
  .flyer {
    position: absolute; left: 51px; top: 26px;
    width: 830px; height: 1148px;
    background: var(--paper); overflow: hidden;
    font-family: "Lato", sans-serif; color: var(--ink);
  }
  .flyer-art { position: absolute; inset: 0; }

  .phone { position: absolute; left: 62px; top: 32px; display: flex; align-items: center; gap: 18px; }
  .phone-icon { width: 44px; height: 44px; }
  .phone-number { font-family: "Roboto Condensed", sans-serif; font-weight: 700; font-size: 37px; color: #3a3a3a; letter-spacing: 0.5px; }

  .brand-mark { position: absolute; left: 352px; top: 62px; width: 130px; display: flex; align-items: center; gap: 6px; }
  .brand-mark-dot { width: 10px; height: 10px; background: var(--green-dark); flex: none; }
  .brand-mark-name { font-family: "Lato", sans-serif; font-weight: 700; font-size: 10px; line-height: 1.25; color: var(--green-dark); letter-spacing: 0.5px; }

  .name-box {
    position: absolute; left: 25px; top: 90px; width: 316px; height: 89px;
    background: var(--green-dark); box-shadow: 6px 6px 0 #9a9a9a;
    display: flex; align-items: center; justify-content: center;
  }
  .name-box-text { font-family: "Roboto Condensed", sans-serif; font-weight: 700; font-size: 66px; color: #fff; line-height: 1; }
  .name-sub { position: absolute; left: 33px; top: 186px; font-family: "Roboto Condensed", sans-serif; font-weight: 700; font-size: 38px; color: var(--green-dark); }
  .tagline { position: absolute; left: 43px; top: 245px; font-size: 22px; line-height: 1.3; color: var(--ink); }

  .headline { position: absolute; left: 520px; top: 40px; width: 260px; text-align: center; font-family: "Roboto Condensed", sans-serif; font-weight: 700; font-size: 26px; line-height: 1.25; color: #fff; }
  .benefits { position: absolute; left: 516px; top: 116px; list-style: none; }
  .benefits li { font-family: "Lato", sans-serif; font-weight: 700; font-size: 22px; line-height: 28px; color: var(--ink); display: flex; align-items: center; gap: 10px; }
  .benefits svg { width: 12px; height: 12px; flex: none; }

  .services-intro { position: absolute; left: 31px; top: 782px; width: 200px; font-weight: 900; font-size: 19px; line-height: 1.1; color: var(--green-dark); }
  .service-pill {
    position: absolute; left: 38px; width: 135px;
    background: var(--teal); color: #fff; border-radius: 18px;
    font-size: 14px; line-height: 1.05; text-align: center;
    display: flex; align-items: center; justify-content: center;
  }

  .coupons-title { position: absolute; left: 340px; top: 795px; width: 330px; text-align: center; font-weight: 700; font-size: 58px; color: #fff; letter-spacing: 1px; }

  .coupon {
    position: absolute; background: #fff; border: 2px solid #cfe3b3;
    display: flex; box-shadow: 0 2px 4px rgba(0,0,0,0.15);
  }
  .coupon-stub { width: 22px; background: var(--green); display: flex; align-items: center; justify-content: center; }
  .coupon-stub.is-blue { background: var(--teal); }
  .coupon-stub span { writing-mode: vertical-rl; transform: rotate(180deg); font-size: 8px; color: #fff; letter-spacing: 0.5px; }
  .coupon-body { flex: 1; display: flex; flex-direction: column; align-items: center; justify-content: center; gap: 3px; padding: 4px; }
  .coupon-code { font-size: 9px; color: var(--muted); letter-spacing: 0.5px; }
  .coupon-title { font-weight: 700; font-size: 14px; line-height: 1.05; text-align: center; color: var(--green-dark); }
  .coupon-title.is-blue { color: var(--teal); font-size: 11px; }
  .coupon-value { font-weight: 900; font-size: 21px; color: var(--green-dark); border: 2px solid #f2d25a; padding: 0 6px; }

  .web { position: absolute; left: 0; width: 830px; top: 1102px; display: flex; justify-content: center; align-items: center; gap: 7px; font-size: 13px; letter-spacing: 2px; color: #fff; }
  .web-dot { width: 11px; height: 11px; border-radius: 50%; background: #fff; }
</style>
</head>
<body>
<main class="flyer">
  <svg class="flyer-art" viewBox="0 0 830 1148" width="830" height="1148" aria-hidden="false">
    <defs>
      <linearGradient id="room-tones" x1="0" y1="0" x2="0" y2="1">
        <stop offset="0" stop-color="#f4f5f2"/>
        <stop offset="0.65" stop-color="var(--photo-light)"/>
        <stop offset="1" stop-color="#a9bf6a"/>
      </linearGradient>
      <linearGradient id="worker-tones" x1="0" y1="0" x2="1" y2="1">
        <stop offset="0" stop-color="#f1f1ee"/>
        <stop offset="1" stop-color="#c9cfc0"/>
      </linearGradient>
    </defs>

    <!-- green info panel -->
    <polygon points="509,26 803,26 803,812 701,1118 185,1118" fill="var(--green)"/>
    <!-- diagonal accent strips -->
    <polygon points="470,26 478,26 212,1000 204,1000" fill="var(--teal)"/>
    <polygon points="440,210 464,210 432,330 408,330" fill="var(--teal)"/>
    <polygon points="348,255 370,255 340,360 318,360" fill="var(--teal)"/>
    <polygon points="236,730 262,730 240,800 214,800" fill="var(--teal)"/>
    <polygon points="660,680 745,680 720,780 635,780" fill="var(--cyan)"/>
    <polygon points="700,560 716,560 690,640 674,640" fill="var(--cyan)"/>
    <polygon points="790,500 803,500 803,560 772,700 758,700" fill="var(--cyan)"/>
    <polygon points="806,760 813,760 813,1000 770,1140 763,1140" fill="var(--teal)"/>

    <!-- photo panels -->
    <polygon points="25,338 287,338 221,692 25,692" fill="url(#worker-tones)" role="img" aria-label="Photo: cleaner in apron and gloves in a bright living room"/>
    <polygon points="315,256 589,256 503,768 217,768" fill="#fff"/>
    <polygon points="325,268 575,268 493,756 229,756" fill="url(#room-tones)" role="img" aria-label="Photo: cleaner dusting shelves in a white living room with green rug"/>
    <polygon points="533,332 791,332 791,692 485,692" fill="url(#worker-tones)" role="img" aria-label="Photo: cleaners tidying a sofa in a sunlit room"/>

    <!-- footer rule -->
    <line x1="290" y1="1086" x2="620" y2="1086" stroke="rgba(0,0,0,0.25)" stroke-width="2"/>
  </svg>

  <div class="phone">
    <svg class="phone-icon" viewBox="0 0 44 44" aria-hidden="true">
      <circle cx="22" cy="22" r="22" fill="#3a3a3a"/>
      <path d="M15 12c1-1 2-1 3 0l3 4c1 1 0 2-1 3l-1 1c1 3 4 6 7 7l1-1c1-1 2-2 3-1l4 3c1 1 1 2 0 3l-2 2c-2 2-8 0-13-5s-7-11-5-13z" fill="#fff"/>
    </svg>
    <span class="phone-number">318.492.5063</span>
  </div>

  <div class="brand-mark">
    <span class="brand-mark-dot"></span>
    <span class="brand-mark-name">VELMOND CLEANING SERVICES</span>
  </div>

  <div class="name-box"><span class="name-box-text">Velmond</span></div>
  <div class="name-sub">Cleaning Services</div>
  <p class="tagline">You have better things<br>to do than clean.</p>

  <h2 class="headline">LET US DO THE DIRTY<br>WORK FOR YOU!</h2>
  <ul class="benefits">
    <li><svg viewBox="0 0 12 12"><path d="M2 10 L10 2 M5 2 H10 V7" stroke="#1b4d1b" stroke-width="2" fill="none"/></svg>Satisfaction guaranteed</li>
    <li><svg viewBox="0 0 12 12"><path d="M2 10 L10 2 M5 2 H10 V7" stroke="#1b4d1b" stroke-width="2" fill="none"/></svg>Flexible scheduling</li>
    <li><svg viewBox="0 0 12 12"><path d="M2 10 L10 2 M5 2 H10 V7" stroke="#1b4d1b" stroke-width="2" fill="none"/></svg>Affordable pricing</li>
    <li><svg viewBox="0 0 12 12"><path d="M2 10 L10 2 M5 2 H10 V7" stroke="#1b4d1b" stroke-width="2" fill="none"/></svg>Hight quality service</li>
  </ul>

  <p class="services-intro">Other Specialty cleaning services available such as:</p>
  <div class="service-pill" style="top:854px;height:31px;">Full house cleaning</div>
  <div class="service-pill" style="top:893px;height:36px;">Professional<br>organizing</div>
  <div class="service-pill" style="top:940px;height:33px;">Window Cleaning</div>
  <div class="service-pill" style="top:986px;height:33px;">Blind cleaning</div>
  <div class="service-pill" style="top:1036px;height:33px;">Event cleaning.</div>

  <h2 class="coupons-title">COUPONS:</h2>

  <div class="coupon" style="left:253px;top:864px;width:229px;height:95px;">
    <div class="coupon-stub"><span>EXP 11/17/19</span></div>
    <div class="coupon-body">
      <span class="coupon-code">CODE 7777</span>
      <span class="coupon-title">HOME CLEANING</span>
      <span class="coupon-value">$25.00 OFF</span>
    </div>
    <div class="coupon-stub"><span>EXP 11/17/19</span></div>
  </div>

  <div class="coupon" style="left:494px;top:866px;width:222px;height:92px;">
    <div class="coupon-body">
      <span class="coupon-code">CODE 7778</span>
      <span class="coupon-title is-blue">PROFESSIONAL<br>ORGANIZING</span>
      <span class="coupon-value">$20.00 OFF</span>
    </div>
    <div class="coupon-stub is-blue"><span>EXP 11/17/19</span></div>
  </div>

  <div class="coupon" style="left:360px;top:974px;width:221px;height:90px;">
    <div class="coupon-body">
      <span class="coupon-code">CODE 7779</span>
      <span class="coupon-title">WINDOW CLEANING</span>
      <span class="coupon-value">$30.00 OFF</span>
    </div>
    <div class="coupon-stub"><span>EXP 11/17/19</span></div>
  </div>

  <div class="web"><span class="web-dot"></span>Velmondcleaning.com</div>
</main>
</body>
</html>
```